Brightwell Holdings -Business Card Design Project

I have a new logo to put onto business cards - attached
The word doc shows how I want it all laid out - front page and rear
The lettering I want is clean and rounded - modern
Updates
Project Deadline Extended
Reason: There was no original deadline!
Target Market(s)
25-49 year old leaders and entrepreneurs in Australia
Industry/Entity Type
Business

```html
<!DOCTYPE html>
<html lang="en">
<head>
<meta charset="utf-8">
<title>Brightwell Holdings – Business Cards</title>
<link rel="stylesheet" href="https://fonts.googleapis.com/css2?family=Lato:wght@400;700&display=swap">
<style>
  :root {
    --page-bg: #e9eaec;
    --card-bg: #ffffff;
    --brand-blue: #1f5fae;
    --accent-grey: #a9abae;
    --ink: #1d1d1f;
    --white: #ffffff;
  }
  * { box-sizing: border-box; margin: 0; padding: 0; }
  html, body {
    width: 1200px; height: 926px; overflow: hidden;
    background: var(--page-bg);
    font-family: "Lato", sans-serif;
    color: var(--ink);
  }
  .canvas { position: relative; width: 1200px; height: 926px; }
  .card {
    position: absolute; left: 240px;
    width: 720px; height: 411px;
    background: var(--card-bg);
    box-shadow: 0 2px 10px rgba(0,0,0,0.12);
    overflow: hidden;
  }
  .card--cover { top: 34px; }
  .card--contact { top: 481px; }

  /* Cover side */
  .cover-brand {
    position: absolute; top: 78px; left: 0; width: 100%;
    display: flex; justify-content: center; align-items: center; gap: 14px;
  }
  .brand-square { width: 22px; height: 22px; background: var(--brand-blue); }
  .brand-name {
    font-size: 40px; font-weight: 700; letter-spacing: 2px;
    color: var(--brand-blue); text-transform: uppercase;
  }
  .cover-band { position: absolute; left: 0; top: 160px; width: 720px; height: 251px; }
  .cover-tagline {
    position: absolute; top: 250px; left: 0; width: 100%;
    text-align: center; color: var(--white);
    font-size: 30px; line-height: 1.3;
  }

  /* Contact side */
  .person { position: absolute; left: 48px; top: 44px; }
  .person-name { font-size: 30px; color: var(--brand-blue); }
  .person-role { font-size: 20px; color: var(--ink); letter-spacing: 0.5px; }
  .services {
    position: absolute; left: 48px; top: 100px;
    list-style: none; font-size: 18px; line-height: 1.3;
  }
  .contacts {
    position: absolute; left: 48px; top: 262px;
    list-style: none; font-size: 18px; line-height: 1.55;
  }
  .contacts li { display: flex; align-items: center; gap: 9px; }
  .contacts svg { width: 17px; height: 17px; flex: none; }
  .contact-brand {
    position: absolute; right: 36px; top: 280px;
    display: flex; align-items: center; gap: 10px;
  }
  .contact-brand .brand-name { font-size: 28px; letter-spacing: 1px; }
  .contact-brand .brand-square { width: 16px; height: 16px; }
  .abn { position: absolute; right: 56px; top: 338px; font-size: 19px; }
</style>
</head>
<body>
<main class="canvas">

  <section class="card card--cover" aria-label="Business card front">
    <div class="cover-brand">
      <span class="brand-square"></span>
      <span class="brand-name">Brightwell Holdings</span>
    </div>
    <svg class="cover-band" viewBox="0 0 720 251" preserveAspectRatio="none" aria-hidden="true">
      <path d="M0 20 Q360 -18 720 20 L720 251 L0 251 Z" fill="var(--accent-grey)" opacity="0.55"/>
      <path d="M0 26 Q360 -10 720 26 L720 251 L0 251 Z" fill="var(--brand-blue)"/>
      <path d="M350 8 L370 8 L360 22 Z" fill="var(--accent-grey)"/>
    </svg>
    <p class="cover-tagline">Direction and Growth<br>For Leaders and Entrepreneurs</p>
  </section>

  <section class="card card--contact" aria-label="Business card back">
    <div class="person">
      <span class="person-name">Rowan Hale</span>
      <span class="person-role">&nbsp;-DIRECTOR</span>
    </div>
    <ul class="services">
      <li>NLP Practitioner &amp; Coach</li>
      <li>Personal, Business &amp; Staff Development</li>
      <li>Self Resilience Programs</li>
    </ul>
    <ul class="contacts">
      <li>
        <svg viewBox="0 0 16 16" aria-hidden="true"><rect width="16" height="16" rx="2" fill="var(--brand-blue)"/><path d="M4 5 Q8 2 12 5 L11 7 L9.5 6 L9.5 7.5 L11.5 9.5 L11.5 12 L4.5 12 L4.5 9.5 L6.5 7.5 L6.5 6 L5 7 Z" fill="var(--white)"/></svg>
        0412 555 018
      </li>
      <li>
        <svg viewBox="0 0 16 16" aria-hidden="true"><rect width="16" height="16" rx="2" fill="var(--brand-blue)"/><rect x="3" y="4" width="10" height="7" fill="none" stroke="var(--white)" stroke-width="1.4"/><rect x="6" y="12" width="4" height="1.4" fill="var(--white)"/></svg>
        brightwellholdings.com.au
      </li>
      <li>
        <svg viewBox="0 0 16 16" aria-hidden="true"><rect width="16" height="16" rx="2" fill="var(--brand-blue)"/><rect x="3" y="4.5" width="10" height="7" fill="none" stroke="var(--white)" stroke-width="1.3"/><path d="M3 4.5 L8 8.5 L13 4.5" fill="none" stroke="var(--white)" stroke-width="1.3"/></svg>
        rowan@brightwellholdings.com.au
      </li>
    </ul>
    <div class="contact-brand">
      <span class="brand-square"></span>
      <span class="brand-name">Brightwell Holdings</span>
    </div>
    <p class="abn">ABN: 12 345 678 901</p>
  </section>

</main>
</body>
</html>
```